Decorative Candle business needs website designed

We are a new decorative candle business, and we need a website designed. We are looking for a modern/elegant feel to the page. We are working on taking pictures of each of our designs, so that we can display all our designs online.

Our target audience is females aged 16-45

We will need online store facilities also, as we plan to see online.

Please feel free to check out our instagram page for an idea of what we do: @wickworkbymirelune

I have attached our logo below for use.

```html
<!DOCTYPE html>
<html lang="en">
<head>
<meta charset="utf-8">
<title>Wickwork by Mirelune</title>
<link rel="stylesheet" href="https://fonts.googleapis.com/css2?family=Source+Sans+3:wght@400;600;700&display=swap">
<style>
:root{
  --ink:#000;
  --paper:#fff;
  --text:#2b2b2b;
  --panel:#e9eaec;
  --panel-line:#dcdde0;
  --accent:#d2692c;
  --flame-light:#e29a4c;
  --flame-dark:#2a1306;
  --muted:#b7b7b7;
  --soc-1:#3b5a9a;
  --soc-2:#3aa4dc;
  --soc-3:#d5302a;
  --soc-4:#f1a73a;
}
*{box-sizing:border-box;margin:0;padding:0}
html,body{width:828px;height:1200px;overflow:hidden;background:var(--paper)}
body{position:relative;font-family:"Source Sans 3",Arial,sans-serif;color:var(--text)}
.abs{position:absolute}

/* header */
.site-header{position:absolute;left:0;top:0;width:828px;height:130px;background:var(--ink);color:var(--paper)}
.brand{position:absolute;left:20px;top:22px;width:92px;text-align:center;font-weight:600;font-size:15px;letter-spacing:2px;line-height:1.05}
.brand small{display:block;font-size:8px;letter-spacing:1px;margin-top:2px}
.brand-dot{display:block;width:12px;height:12px;border-radius:50%;background:var(--soc-4);margin:0 auto 10px}
.social{position:absolute;display:flex;gap:5px}
.social span{width:23px;height:23px;border-radius:50%}
.social span:nth-child(1){background:var(--soc-1)}
.social span:nth-child(2){background:var(--soc-2)}
.social span:nth-child(3){background:var(--soc-3)}
.social span:nth-child(4){background:var(--soc-4)}
.header-social{left:425px;top:42px}
.search{position:absolute;left:587px;top:48px;width:120px;height:21px;background:var(--paper);color:var(--ink);font-size:13px;padding:1px 6px}
.search svg{position:absolute;right:5px;top:3px}
.cart{position:absolute;left:737px;top:44px;display:flex;gap:6px;font-size:10px;font-weight:700;line-height:1.25}
.main-nav{position:absolute;top:83px;left:0;width:828px;font-size:16px;font-weight:700}
.main-nav a{position:absolute;color:var(--paper);text-decoration:none;transform:translateX(-50%)}

/* hero */
.hero{position:absolute;left:0;top:130px;width:828px;height:432px}
.hero-photo{position:absolute;inset:0;background:radial-gradient(ellipse at 30% 40%,var(--flame-light) 0%,#a9561f 35%,#4e2510 70%,var(--flame-dark) 100%)}
.hero-card{position:absolute;left:382px;top:136px;width:389px;height:154px;background:rgba(0,0,0,.93);color:var(--paper);padding:22px 30px}
.hero-card h1{font-size:34px;font-weight:700;line-height:1.1;margin-bottom:8px}
.hero-card p{font-size:19px;line-height:1.3}
.order-btn{position:absolute;left:628px;top:301px;width:124px;height:36px;background:var(--accent);color:var(--paper);font-size:18px;text-align:center;line-height:36px}
.slider-dots{position:absolute;left:368px;top:402px;display:flex;gap:12px}
.slider-dots span{width:14px;height:14px;border-radius:50%;background:var(--paper)}
.slider-dots span.active{background:#8a4a1c}

/* welcome */
.welcome{position:absolute;left:0;top:582px;width:828px;text-align:center}
.welcome h2{font-size:32px;font-weight:400;line-height:1.1;margin-bottom:6px}
.welcome p{font-size:14px;line-height:1.3}

/* new products */
.products{position:absolute;left:11px;top:688px;width:550px;height:335px;border:3px solid var(--panel-line);background:var(--paper)}
.panel-head{background:var(--panel);height:44px;padding:9px 17px;font-size:18px;font-weight:600}
.product{position:absolute;width:102px}
.product .thumb{width:100px;height:86px;background:var(--panel);padding:3px 8px}
.product .thumb div{width:84px;height:80px}
.product p{font-size:12.5px;line-height:1.25;margin-top:8px;padding-left:6px}

/* instagram */
.instagram{position:absolute;left:587px;top:688px;width:224px;height:357px;border:3px solid var(--panel-line);background:var(--paper)}
.instagram .panel-head{height:52px;padding:8px 18px;line-height:1}
.instagram h3{font-size:19px;font-weight:700;color:#444}
.instagram h4{font-size:14px;font-weight:600;color:#444;margin-top:2px}
.insta-photo{position:absolute;width:92px;height:92px}

/* footer */
.site-footer{position:absolute;left:0;top:1069px;width:828px;height:131px;background:var(--ink);color:var(--paper)}
.footer-nav{position:absolute;left:30px;top:16px;font-size:12.5px;display:flex}
.footer-nav span{padding:0 10px;border-left:1px solid var(--paper)}
.footer-nav span:first-child{padding-left:0;border-left:none}
.footer-social{left:615px;top:20px}
.newsletter-label{position:absolute;left:616px;top:59px;font-size:9px;color:var(--muted)}
.newsletter{position:absolute;left:613px;top:76px;display:flex}
.newsletter .field{width:112px;height:22px;background:var(--paper);color:#b06a2a;font-size:9px;padding:5px 6px;border:1px solid var(--muted)}
.newsletter .submit{width:46px;height:22px;background:#2a2a2a;color:var(--paper);font-size:10px;font-weight:600;text-align:center;line-height:22px}
.footer-copy{position:absolute;left:28px;top:80px;font-size:11.5px;color:var(--muted);line-height:1.9}
</style>
</head>
<body>

<header class="site-header">
  <div class="brand"><span class="brand-dot"></span>Wickwork<small>by Mirelune</small></div>
  <div class="social header-social"><span></span><span></span><span></span><span></span></div>
  <div class="search">Search
    <svg width="15" height="15" viewBox="0 0 15 15"><circle cx="6" cy="6" r="4.5" fill="none" stroke="#000" stroke-width="2"/><line x1="9.3" y1="9.3" x2="14" y2="14" stroke="#000" stroke-width="2.4"/></svg>
  </div>
  <div class="cart">
    <svg width="22" height="22" viewBox="0 0 22 22"><path d="M1 3h4l3 11h10l2-8H7" fill="none" stroke="#fff" stroke-width="2"/><circle cx="9" cy="18" r="2" fill="#fff"/><circle cx="17" cy="18" r="2" fill="#fff"/></svg>
    <div>My Cart<br>0 items</div>
  </div>
  <nav class="main-nav">
    <a style="left:146px">Home</a>
    <a style="left:268px">Products</a>
    <a style="left:404px">Store</a>
    <a style="left:536px">Contact</a>
    <a style="left:664px">About</a>
  </nav>
</header>

<section class="hero">
  <div class="hero-photo" role="img" aria-label="Rows of lit white pillar candles glowing warm orange"></div>
  <div class="hero-card">
    <h1>New Candles</h1>
    <p>Neque porro quisquam est qui dolorem ipsum quia dolor sit amet</p>
  </div>
  <div class="order-btn">Order Now</div>
  <div class="slider-dots"><span></span><span class="active"></span><span></span><span></span></div>
</section>

<section class="welcome">
  <h2>Welcome to Wickwork</h2>
  <p>Neque porro quisquam est qui dolorem ipsum quia dolor sit amet<br>Lorem ipsum dolor sit amet, consectetur adipiscing elit.</p>
</section>

<section class="products">
  <div class="panel-head">New Products</div>
  <div class="product" style="left:9px;top:56px"><div class="thumb"><div role="img" aria-label="Decorated candle set" style="background:linear-gradient(#cfc7c6,#3a2a3e)"></div></div><p>Item Name<br>€12,90</p></div>
  <div class="product" style="left:111px;top:56px"><div class="thumb"><div role="img" aria-label="Decorated candle set" style="background:linear-gradient(#d9d1c8,#5a3a2c)"></div></div><p>Item Name<br>€12,90</p></div>
  <div class="product" style="left:213px;top:56px"><div class="thumb"><div role="img" aria-label="Decorated candle set" style="background:linear-gradient(#c9c6c2,#3b2e2a)"></div></div><p>Item Name<br>€12,90</p></div>
  <div class="product" style="left:315px;top:56px"><div class="thumb"><div role="img" aria-label="Decorated candle set" style="background:linear-gradient(#cfcbd2,#3e3450)"></div></div><p>Item Name<br>€12,90</p></div>
  <div class="product" style="left:417px;top:56px"><div class="thumb"><div role="img" aria-label="Candles beside shoes" style="background:linear-gradient(#c9bdb0,#4a3026)"></div></div><p>Item Name<br>€12,90</p></div>
  <div class="product" style="left:9px;top:196px"><div class="thumb"><div role="img" aria-label="Decorated candle set" style="background:linear-gradient(#e3ddd4,#8a6a48)"></div></div><p>Item Name<br>€12,90</p></div>
  <div class="product" style="left:111px;top:196px"><div class="thumb"><div role="img" aria-label="Row of decorated candles" style="background:linear-gradient(#e6e2de,#7a6a58)"></div></div><p>Item Name<br>€12,90</p></div>
  <div class="product" style="left:213px;top:196px"><div class="thumb"><div role="img" aria-label="Decorated candle set" style="background:linear-gradient(#e4d8c6,#8a5a3a)"></div></div><p>Item Name<br>€12,90</p></div>
  <div class="product" style="left:315px;top:196px"><div class="thumb"><div role="img" aria-label="Decorated candle set" style="background:linear-gradient(#e8dcd8,#9a7a70)"></div></div><p>Item Name<br>€12,90</p></div>
  <div class="product" style="left:417px;top:196px"><div class="thumb"><div role="img" aria-label="Candles with packaging" style="background:linear-gradient(#c7c2c4,#6a5a4a)"></div></div><p>Item Name<br>€12,90</p></div>
</section>

<aside class="instagram">
  <div class="panel-head"><h3>INSTAGRAM</h3><h4>Latest Photos</h4></div>
  <div class="insta-photo" role="img" aria-label="Plate of food" style="left:9px;top:57px;background:linear-gradient(135deg,#e8705a,#8a5a48)"></div>
  <div class="insta-photo" role="img" aria-label="Tea set on a table" style="left:106px;top:57px;background:linear-gradient(135deg,#6e6a66,#d8d2cc)"></div>
  <div class="insta-photo" role="img" aria-label="Dessert in a bowl" style="left:9px;top:154px;background:linear-gradient(135deg,#d8cfb8,#8e8670)"></div>
  <div class="insta-photo" role="img" aria-label="Pink heart-shaped box" style="left:106px;top:154px;background:linear-gradient(135deg,#e66aa0,#c04a80)"></div>
  <div class="insta-photo" role="img" aria-label="Pink gift items" style="left:9px;top:251px;background:linear-gradient(135deg,#ecc8d8,#c88aa8)"></div>
  <div class="insta-photo" role="img" aria-label="Staircase with decorations" style="left:106px;top:251px;background:linear-gradient(135deg,#5a5850,#d6d2c8)"></div>
</aside>

<footer class="site-footer">
  <nav class="footer-nav"><span>Home</span><span>Products</span><span>Store</span><span>Contact</span><span>About</span></nav>
  <div class="social footer-social"><span></span><span></span><span></span><span></span></div>
  <div class="newsletter-label">Suscribe To Our Newsletter</div>
  <div class="newsletter"><div class="field">Enter your email</div><div class="submit">Submit</div></div>
  <div class="footer-copy">Lorem ipsum dolor sit amet, consectetur adipiscing elit. Nulla malesuada<br>Copyright 2014 Waxloomshop.nl</div>
</footer>

</body>
</html>
```